"Calm Harbor Circle" Coaching Website Needs a Wordpress Design

"Calm Harbor Circle' is a Coaching Website that helps mothers find happiness, freedom, and connection in motherhood.

My website is www.CalmHarborCircle.com

I made the website myself and now would like to get this website professionally designed. I would also like the winner to code the designs and MIGRATE THESE FILES to my Wordpress website. I would like to get designs for ALL 7 PAGES. Due to the 7 pages and the migrating work, I chose the $699 package.

I am including files for the logo and all the pictures and drawings of the website. I am also including some other "women experiencing freedom" pictures to give the kind of "freedom" feel I would like. I will get a new profile picture done after I have my design.

The Feel of my Website:
My motto is that I help mothers "STEP BEYOND THE NEST" to find HAPPINESS, FREEDOM, and CONNECTION in motherhood.
I help mothers be happier by helping them FREE themselves from the societal constraints of motherhood and I help them CONNECT better with other mothers. I have, therefore, attempted to portray Freedom, Connection, and Happiness as emotional benefits.

I made my own logo that corresponds to my videos.

The Rainbow-Freedom picture at the top does not have to stay. I just put it there as an example.

Regarding the Colour:
I have made my own whiteboard videos and corresponding logo and drawings throughout. I used red, blue, green, (and a little bit of purple, yellow, and brown) in my videos due to the fact that they are whiteboard videos. I am having trouble deciding which colours to use for my website in general considering that I have already used these colours in my videos, and drawings. I am not visual and I have NO talent in design. I would love to get YOUR input in what colours to use and everything else design-wise.

My only Design Requirement:
My main requirement is that the header part not take too much space. I want people to immediately see the videos and other content right when they land on the page. I don't want them to have to scroll down.

Thank you so much!! :-)

Target Market(s)

I target DEPRESSED, ANXIOUS, and UNHAPPY mothers, and I help them find HAPPINESS, FREEDOM, and CONNECTION in motherhood.

Industry/Entity Type

Life Coaching

Coding

Coded - Design and coding required

Number of Pages Required

5+ page

Requirements
Must have
• - Please look at my website at www.CalmHarborCircle.com
• - I would like these 7 pages designed.
• - I would like the coded files to be migrated to my website
• - My main requirement is that the header part not take too much space. I want people to immediately see the videos and other content right when they land on the page. I don't want them to have to scroll down.
Nice to have
• - I would ideally like the website to portray the emotional benefits of FREEDOM and CONNECTION. My motto is that I help mothers STEP BEYOND THE NEST to find HAPPINESS, FREEDOM, and CONNECTION in motherhood. I showed this in the logo that I made. :-)
• - The Rainbow-Freedom picture at the top does NOT have to stay if you would prefer to do something else.

```html
<!DOCTYPE html>
<html lang="en">
<head>
<meta charset="utf-8">
<title>Calm Harbor Circle</title>
<link href="https://fonts.googleapis.com/css2?family=Oswald:wght@500;600&family=Cabin:wght@400;500;600&family=Open+Sans:wght@400;600&display=swap" rel="stylesheet">
<style>
:root{
  --red:#d2232a;
  --blue:#1b34ab;
  --navy:#13268a;
  --white:#ffffff;
  --text:#555a63;
  --dark:#2b2b2b;
  --sun:#f6c23e;
  --field:#eceef2;
  --line:#c9ccd3;
  --footer:#f2f3f7;
}
*{box-sizing:border-box;margin:0;padding:0}
html,body{width:1200px;height:4072px;overflow:hidden}
body{position:relative;background:var(--white);font-family:"Open Sans",Arial,sans-serif;color:var(--text)}
section,header,nav,footer{position:absolute;left:0;width:1200px}
.abs{position:absolute}
.btn{position:absolute;display:flex;align-items:center;justify-content:center;background:var(--red);color:var(--white);font-family:"Cabin",sans-serif;font-weight:500;font-size:20px;text-transform:uppercase;letter-spacing:.5px}
.brand{display:flex;align-items:center;gap:12px;font-family:"Cabin",sans-serif;font-weight:600;color:var(--blue)}
.brand .mark{width:34px;height:34px;background:var(--red)}
.social{display:flex;gap:10px}
.social span{width:34px;height:34px;border-radius:50%;background:var(--blue)}
.social span:nth-child(even){background:var(--red)}
.section-title{font-family:"Cabin",sans-serif;font-weight:400;font-size:46px;letter-spacing:.5px;text-transform:uppercase}
.section-title .r{color:var(--red)}
.section-title .b{color:var(--blue)}
p.body{font-size:15px;line-height:26px}

/* hero */
.hero{top:0;height:673px;background:linear-gradient(180deg,#f7d24a 0%,#f0a93a 38%,#d9922f 62%,#c98a2e 100%)}
.hero-photo{position:absolute;inset:0;background:radial-gradient(circle at 30% 30%,rgba(255,248,200,.85),rgba(255,220,120,.2) 45%,transparent 70%),linear-gradient(90deg,rgba(60,120,200,.35),transparent 40%,transparent 70%,rgba(120,90,40,.3))}
.hero .brand{left:80px;top:22px;font-size:30px}
.hero .phone{right:80px;top:22px;display:flex;align-items:center;gap:10px;font-family:"Cabin",sans-serif;font-size:26px;color:var(--blue)}
.hero .social{position:absolute;right:80px;top:66px}
.hero h1{position:absolute;left:80px;top:290px;font-family:"Oswald",sans-serif;font-weight:600;font-size:56px;line-height:70px;color:var(--dark);letter-spacing:.5px}
.hero .lead{position:absolute;left:80px;top:372px;width:1040px;font-size:15px;line-height:23px;color:var(--white);text-shadow:0 1px 2px rgba(0,0,0,.35)}
.hero .btn-main{left:80px;top:462px;width:175px;height:56px}
.hero .btn-ghost{left:265px;top:462px;width:192px;height:56px;background:transparent;border:2px solid var(--sun);color:var(--dark)}
.hero .arrow{position:absolute;top:330px}

/* nav */
.main-nav{top:673px;height:63px;background:var(--blue);display:flex;align-items:center;padding-left:76px}
.main-nav a{font-family:"Cabin",sans-serif;font-size:17px;color:var(--white);text-decoration:none;text-transform:uppercase;height:63px;display:flex;align-items:center;padding:0 16px}
.main-nav a.active{background:var(--red);padding:0 22px}

/* welcome */
.welcome{top:736px;height:526px;text-align:center}
.welcome .brand{position:absolute;left:50%;transform:translateX(-50%);top:60px;font-size:24px}
.welcome .brand .mark{width:26px;height:26px}
.welcome .section-title{position:absolute;top:128px;width:100%}
.welcome .copy{position:absolute;left:160px;width:880px;top:200px}
.welcome .copy p{margin-bottom:14px}

/* products */
.products{top:1262px;height:747px;background:linear-gradient(160deg,#2b49c8 0%,#1f3aa8 35%,#3a2f9a 60%,#8f4fb0 85%,#c27fa8 100%)}
.products .scene{position:absolute;inset:0;background:radial-gradient(ellipse at 55% 40%,rgba(255,255,255,.35),transparent 55%)}
.products .section-title{position:absolute;top:218px;width:100%;text-align:center;color:var(--white)}
.products .intro{position:absolute;top:284px;width:100%;text-align:center;color:var(--white);font-size:15px}
.service{position:absolute;top:356px;width:300px;text-align:center}
.service .disc{position:relative;margin:0 auto;width:212px;height:212px;border-radius:50%;background:var(--white)}
.service .disc .art{position:absolute;left:38px;top:44px;width:136px;height:124px;background:linear-gradient(135deg,#e9edf5,#cfd6e6)}
.service .num{position:absolute;left:6px;top:-8px;width:52px;height:52px;border-radius:50%;background:var(--red);color:var(--white);font-family:"Cabin",sans-serif;font-size:28px;display:flex;align-items:center;justify-content:center}
.service h3{margin-top:22px;height:52px;font-family:"Cabin",sans-serif;font-weight:500;font-size:16px;line-height:24px;color:var(--white);text-transform:uppercase}
.service .btn{position:relative;margin:20px auto 0;width:163px;height:54px}

/* video */
.video{position:absolute;left:312px;top:1121px;width:576px;height:313px;background:#1d1d1d;border:3px solid #111}
.video .frame{position:absolute;left:6px;top:6px;right:6px;bottom:34px;background:linear-gradient(180deg,#f7f7f7,#e5e8ee)}
.video .title{position:absolute;left:10px;top:8px;font-size:13px;color:#444}
.video .play{position:absolute;left:50%;top:44%;transform:translate(-50%,-50%)}
.video .bar{position:absolute;left:0;right:0;bottom:0;height:30px;background:#111}
.video .track{position:absolute;left:44px;right:70px;top:13px;height:4px;background:#555}

/* about */
.about{top:2009px;height:448px}
.about .section-title{position:absolute;left:80px;top:60px}
.about .copy{position:absolute;left:80px;top:128px;width:630px}
.about .copy p{font-size:14px;line-height:24px;margin-bottom:10px}
.about .btn{left:80px;top:350px;width:167px;height:54px}
.about .photo{position:absolute;left:741px;top:63px;width:380px;height:318px;background:linear-gradient(135deg,#b9a48f,#8f7866 55%,#c6b3a2)}
.about .portrait{position:absolute;left:692px;top:272px;width:114px;height:114px;border-radius:50%;border:4px solid var(--white);background:linear-gradient(135deg,#c9b6a0,#8c7a68)}

/* subscribe */
.subscribe{top:2457px;height:516px;background:linear-gradient(100deg,#f3b07a 0%,#ea7d50 25%,#dc4a37 50%,#d22b2d 75%,#cf2a2e 100%)}
.subscribe .figure{position:absolute;left:0;top:0;width:360px;height:516px;background:radial-gradient(ellipse at 40% 40%,rgba(255,235,210,.6),transparent 65%)}
.subscribe .headline{position:absolute;left:320px;width:820px;top:56px;text-align:center;color:var(--white);font-size:19px;line-height:30px}
.subscribe .gifts{position:absolute;left:528px;top:150px;display:flex;align-items:center;gap:14px}
.subscribe .gift{width:118px;height:134px;background:rgba(255,255,255,.85)}
.subscribe .plus{color:var(--white);font-size:34px}
.subscribe .note{position:absolute;left:320px;width:820px;top:324px;text-align:center;color:var(--white);font-size:15px;line-height:24px}
.subscribe .field{position:absolute;left:440px;top:394px;width:429px;height:54px;background:var(--white);font-size:14px;color:#888;padding:0 16px;display:flex;align-items:center}
.subscribe .btn{left:877px;top:394px;width:176px;height:54px}

/* contact */
.contact{top:2973px;height:537px;text-align:center}
.contact .section-title{position:absolute;top:64px;width:100%}
.contact .figure{display:inline-block;width:38px;height:54px;vertical-align:middle;margin:0 18px;background:linear-gradient(#eee,#ddd)}
.contact .intro{position:absolute;top:140px;left:300px;width:600px;font-size:15px;line-height:26px}
.contact .accent{position:absolute;top:212px;width:100%;color:var(--red);font-size:17px}
.contact .field{position:absolute;left:217px;width:380px;height:44px;border:1px solid var(--line);background:var(--field);font-size:14px;color:#777;text-align:left;padding:12px 14px}
.contact .message{position:absolute;left:605px;top:252px;width:378px;height:155px;border:1px solid var(--line);background:var(--field);font-size:14px;color:#777;text-align:left;padding:12px 14px}
.contact .btn{left:502px;top:421px;width:193px;height:54px}

/* cheat sheet band */
.cheat{top:3510px;height:210px;background:var(--blue)}
.cheat .flag{position:absolute;left:0;top:0}
.cheat .sheet{position:absolute;left:150px;top:36px;width:72px;height:96px;background:var(--white)}
.cheat h2{position:absolute;left:407px;top:54px;font-family:"Cabin",sans-serif;font-weight:500;font-size:25px;color:var(--white)}
.cheat .field{position:absolute;left:407px;top:110px;width:416px;height:50px;background:var(--white);font-size:14px;color:#888;padding:0 16px;display:flex;align-items:center;justify-content:space-between}
.cheat .btn{left:834px;top:110px;width:219px;height:50px}

/* footer */
.site-footer{top:3720px;height:285px;background:linear-gradient(180deg,var(--footer),#e3e7ef)}
.site-footer .brand{position:absolute;left:80px;top:108px;font-size:22px}
.site-footer .brand .mark{width:26px;height:26px}
.site-footer .social{position:absolute;left:80px;top:168px}
.site-footer h4{font-family:"Cabin",sans-serif;font-weight:600;font-size:17px;color:var(--blue);text-transform:uppercase;margin-bottom:14px}
.col{position:absolute;top:40px}
.links{left:348px}
.links li{list-style:none;font-size:14px;line-height:24px;color:var(--dark);display:flex;align-items:center;gap:10px}
.links li::before{content:"";width:8px;height:8px;background:var(--red)}
.blog{left:597px;width:250px}
.post{display:flex;gap:12px;margin-bottom:16px}
.post .thumb{flex:none;width:54px;height:54px;border-radius:50%;background:linear-gradient(135deg,#d9c8b8,#a08a78)}
.post p{font-size:12px;line-height:18px;color:var(--dark);text-transform:uppercase}
.post .more{color:var(--red);text-transform:none;font-size:13px}
.touch{left:874px;width:250px}
.touch .item{display:flex;gap:10px;font-size:13px;line-height:20px;color:var(--dark);margin-bottom:12px}
.touch .item svg{flex:none;margin-top:2px}
.touch strong{color:var(--blue);font-weight:600}

.copyright{top:4005px;left:0;width:1200px;height:67px;background:var(--blue);display:flex;align-items:center;justify-content:center;color:var(--white);font-size:14px}
.copyright span{color:var(--red)}
</style>
</head>
<body>

<header class="hero">
  <div class="hero-photo" role="img" aria-label="Woman with arms spread in a golden field under a rainbow and warm sunlight"></div>
  <div class="brand abs"><span class="mark"></span>Calm Harbor Circle</div>
  <div class="phone abs">
    <svg width="22" height="22" viewBox="0 0 24 24"><path fill="#1b34ab" d="M6.6 10.8a15 15 0 0 0 6.6 6.6l2.2-2.2c.3-.3.7-.4 1-.2 1.1.4 2.3.6 3.6.6.6 0 1 .4 1 1V20c0 .6-.4 1-1 1A17 17 0 0 1 3 4c0-.6.4-1 1-1h3.5c.6 0 1 .4 1 1 0 1.3.2 2.5.6 3.6.1.3 0 .7-.2 1z"/></svg>
    (555) 014-2290
  </div>
  <div class="social"><span></span><span></span><span></span><span></span><span></span></div>
  <svg class="arrow" style="left:22px" width="20" height="40" viewBox="0 0 20 40"><path d="M16 4 4 20l12 16" stroke="#fff" stroke-width="3" fill="none"/></svg>
  <svg class="arrow" style="right:22px" width="20" height="40" viewBox="0 0 20 40"><path d="M4 4l12 16L4 36" stroke="#fff" stroke-width="3" fill="none"/></svg>
  <h1>STEP BEYOND THE NEST</h1>
  <div class="lead">The REAL CAUSE of Depression, Anxiety, and Emotional Distress in Motherhood<br>My 6-Step Process of How to ESCAPE these Emotions The MYTHS that our Society Tells<br>Mothers, and Why They are FALSE &nbsp;How You can CONNECT on a Deeper Level with Other Mothers</div>
  <div class="btn btn-main">Know More</div>
  <div class="btn btn-ghost">Contact Us</div>
</header>

<nav class="main-nav">
  <a class="active">Home</a><a>About Me</a><a>Step Beyond the Nest!</a><a>FAQs</a><a>Products/Services</a><a>Contact Me</a><a>Blog</a>
</nav>

<section class="welcome">
  <div class="brand"><span class="mark"></span>Calm Harbor Circle</div>
  <h2 class="section-title"><span class="r">Welcome to </span><span class="b">Calm Harbor Circle</span></h2>
  <div class="copy">
    <p class="body">Dana Whitfield is a Certified Professional Coach who helps mothers be happier in motherhood by helping them escape from the harmful aspects of our mothering culture. She is also the mother of four children ranging from 3 to 8.5 years old.</p>
    <p class="body">Dana grew up in Victoria, Canada. She originally got a Social Science degree in Linguistics due to her fascination with foreign languages and cultures. She lived in 7 foreign cultures in her twenties (Quebec, France, Holland, Germany, Belgium, Switzerland, and Hungary), where she lived with the locals and spoke their languages.</p>
  </div>
</section>

<section class="products">
  <div class="scene" role="img" aria-label="Woman leaping joyfully against a blue sky with a rainbow"></div>
  <h2 class="section-title"><span class="r">Products</span>/Services</h2>
  <div class="intro">I am currently offering the following services</div>
  <div class="service" style="left:113px">
    <div class="disc"><div class="art" role="img" aria-label="Whiteboard drawing for the coaching program"></div><div class="num">1</div></div>
    <h3>6-to-12 week "Step Beyond<br>the Nest" coaching program</h3>
    <div class="btn">Know More</div>
  </div>
  <div class="service" style="left:447px">
    <div class="disc"><div class="art" role="img" aria-label="Whiteboard drawing for graduate coaching"></div><div class="num">2</div></div>
    <h3>Graduate coaching - life<br>beyond the nest!</h3>
    <div class="btn">Know More</div>
  </div>
  <div class="service" style="left:798px">
    <div class="disc"><div class="art" role="img" aria-label="Whiteboard drawing of a laptop showing a free email course"></div><div class="num">3</div></div>
    <h3>Free "Step Beyond the Nest"<br>email course</h3>
    <div class="btn">Know More</div>
  </div>
</section>

<div class="video">
  <div class="frame" role="img" aria-label="Whiteboard video still: stack of books and a television"></div>
  <div class="title">The Real Cause of Postpartum Depression and Anxiety</div>
  <svg class="play" width="70" height="50" viewBox="0 0 70 50"><rect width="70" height="50" rx="12" fill="#d2232a"/><path d="M28 15v20l17-10z" fill="#fff"/></svg>
  <div class="bar">
    <svg style="position:absolute;left:14px;top:8px" width="14" height="14" viewBox="0 0 14 14"><rect x="2" y="1" width="3" height="12" fill="#fff"/><rect x="9" y="1" width="3" height="12" fill="#fff"/></svg>
    <div class="track"></div>
    <svg style="position:absolute;right:14px;top:7px" width="16" height="16" viewBox="0 0 16 16"><path d="M1 5V1h4M11 1h4v4M15 11v4h-4M5 15H1v-4" stroke="#fff" stroke-width="2" fill="none"/></svg>
  </div>
</div>

<section class="about">
  <h2 class="section-title"><span class="r">About </span><span class="b">Me</span></h2>
  <div class="copy">
    <p class="body">Dana Whitfield is a Certified Professional Coach who helps mothers be happier in motherhood by helping them escape from the harmful aspects of our mothering culture. She is also the mother of four children ranging from 3 to 8.5 years old.</p>
    <p class="body">Dana grew up in Victoria, Canada. She originally got a Social Science degree in Linguistics due to her fascination with foreign languages and cultures. She lived in 7 foreign cultures in her twenties (Quebec, France, Holland, Germany, Belgium, Switzerland, and Hungary), where she lived with the locals and spoke their languages.</p>
  </div>
  <div class="btn">Know More</div>
  <div class="photo" role="img" aria-label="Family photo of a mother with her children"></div>
  <div class="portrait" role="img" aria-label="Portrait of the coach"></div>
</section>

<section class="subscribe">
  <div class="figure" role="img" aria-label="Woman with head tilted back and arms open in warm sunlight"></div>
  <div class="headline">DEPRESSED, ANXIOUS, and UNHAPPY mothers, and I help them find HAPPINESS,<br>FREEDOM, and CONNECTION in motherhood.</div>
  <div class="gifts">
    <div class="gift" role="img" aria-label="Drawing of a free cheat sheet"></div><span class="plus">+</span>
    <div class="gift" role="img" aria-label="Drawing of a free video"></div><span class="plus">+</span>
    <div class="gift" role="img" aria-label="Drawing of a free email course"></div>
  </div>
  <div class="note">To Receive Your Free CHEAT SHEET, a Copy of this Video, and a Subscription<br>to my Free Email Course...</div>
  <div class="field">Enter Your Email*</div>
  <div class="btn">Subscribe</div>
</section>

<section class="contact">
  <h2 class="section-title"><span class="figure" role="img" aria-label="Stick figure drawing"></span><span class="r">Contact </span><span class="b">Us</span><span class="figure" role="img" aria-label="Stick figure drawing"></span></h2>
  <p class="intro">Find Out How My "STEP BEYOND THE NEST" PROGRAM can Help YOU Find Happiness, Freedom, and Connection in Motherhood!</p>
  <div class="accent">I am Looking Forward to Talking with You!</div>
  <div class="field" style="top:252px">Name*</div>
  <div class="field" style="top:307px">Email*</div>
  <div class="field" style="top:362px">Subject*</div>
  <div class="message">Message*</div>
  <div class="btn">Send to Dana</div>
</section>

<section class="cheat">
  <svg class="flag" width="380" height="210" viewBox="0 0 380 210"><path d="M0 0h330l50 105-50 105H0z" fill="#d2232a"/></svg>
  <div class="sheet" role="img" aria-label="Drawing of a free cheat sheet held by stick figures"></div>
  <h2>Enter Your Email Address to Receive Your Free Cheet Sheet</h2>
  <div class="field">Enter Your Email id*
    <svg width="20" height="16" viewBox="0 0 20 16"><rect x="1" y="1" width="18" height="14" fill="none" stroke="#d2232a" stroke-width="2"/><path d="M1 1l9 7 9-7" fill="none" stroke="#d2232a" stroke-width="2"/></svg>
  </div>
  <div class="btn">Free Cheet Sheet</div>
</section>

<footer class="site-footer">
  <div class="brand"><span class="mark"></span>Calm Harbor Circle</div>
  <div class="social"><span></span><span></span><span></span><span></span><span></span></div>
  <div class="col links">
    <h4>Usefull Links</h4>
    <ul><li>Home</li><li>About Me</li><li>Step Beyond the Nest</li><li>Faq's</li><li>Products/Services</li><li>Contact Me</li><li>Blog</li></ul>
  </div>
  <div class="col blog">
    <h4>Latest Blog</h4>
    <div class="post"><div class="thumb" role="img" aria-label="Blog post photo"></div><p>You chose to have children (another myth)<br><span class="more">Read More... »</span></p></div>
    <div class="post"><div class="thumb" role="img" aria-label="Blog post photo"></div><p>Embracing that future psycho-logists coach!<br><span class="more">Read More... »</span></p></div>
  </div>
  <div class="col touch">
    <h4>Get in Touch</h4>
    <div class="item"><svg width="14" height="16" viewBox="0 0 14 16"><path d="M7 0a5 5 0 0 1 5 5c0 4-5 11-5 11S2 9 2 5a5 5 0 0 1 5-5z" fill="#d2232a"/></svg><div><strong>CALM HARBOR CIRCLE</strong><br>101 - Lorem ipsum is a simple text of print and type setting.</div></div>
    <div class="item"><svg width="14" height="14" viewBox="0 0 24 24"><path fill="#d2232a" d="M6.6 10.8a15 15 0 0 0 6.6 6.6l2.2-2.2c.3-.3.7-.4 1-.2 1.1.4 2.3.6 3.6.6.6 0 1 .4 1 1V20c0 .6-.4 1-1 1A17 17 0 0 1 3 4c0-.6.4-1 1-1h3.5c.6 0 1 .4 1 1 0 1.3.2 2.5.6 3.6.1.3 0 .7-.2 1z"/></svg><div>(555) 014-2290</div></div>
    <div class="item"><svg width="14" height="14" viewBox="0 0 24 24"><path fill="#d2232a" d="M6.6 10.8a15 15 0 0 0 6.6 6.6l2.2-2.2c.3-.3.7-.4 1-.2 1.1.4 2.3.6 3.6.6.6 0 1 .4 1 1V20c0 .6-.4 1-1 1A17 17 0 0 1 3 4c0-.6.4-1 1-1h3.5c.6 0 1 .4 1 1 0 1.3.2 2.5.6 3.6.1.3 0 .7-.2 1z"/></svg><div>(555) 017-3318</div></div>
    <div class="item"><svg width="14" height="12" viewBox="0 0 20 16"><rect x="1" y="1" width="18" height="14" fill="#d2232a"/><path d="M1 1l9 7 9-7" fill="none" stroke="#fff" stroke-width="2"/></svg><div>Dana@CalmHarborCircle.com</div></div>
  </div>
</footer>

<div class="copyright abs">©<span>Calm Harbor Circle</span>&nbsp;2017. All Rights Reserved</div>

</body>
</html>
```